Featherstones--Wine Bottle Label for Quail Jubilee

We need a design for a wine bottle labels for 2 custom wines that a local winery is producing for our hunting lodge, Quail Jubilee. The lodge restaurant is called "Featherstones", so we'd like to use that as the theme for the label picture. The thought is that we'd use the same design but with different colors for the two types--Red Table Wine and White Table Wine. You can check out our website at www.quailjubilee-example.com for inspiration. Since there are many regulations on what goes on the label bottled alcohol in the US, we are just looking for the artwork to be used on the label.

Industry/Entity Type

Hunting

Font styles to use
Decorative
Script

Requirements
Must have
• Featherstones (as in male US pheasants) should be included in the design.
Nice to have
• It would be nice to have somewhat of an abstract version of a Rooster Pheasant in the design. We would like to see the same design in 2 different color palettes.

```html
<!DOCTYPE html>
<html lang="en">
<head>
<meta charset="utf-8">
<title>Featherstones Wine Labels – Quail Jubilee</title>
<link rel="stylesheet" href="https://fonts.googleapis.com/css2?family=Cinzel:wght@400;700&family=Fascinate+Inline&display=swap">
<style>
  :root {
    --backdrop: #9fb4c9;
    --label-bg: #050708;
    --label-bg-red: #061110;
    --gold: #e2a248;
    --gold-deep: #8a5a20;
    --teal: #63d1ab;
    --teal-deep: #22705a;
  }
  * { box-sizing: border-box; margin: 0; padding: 0; }
  html, body { width: 1200px; height: 706px; overflow: hidden; }
  body {
    background: var(--backdrop);
    display: flex;
    align-items: center;
    justify-content: center;
    gap: 100px;
    font-family: "Cinzel", serif;
  }
  .label {
    position: relative;
    width: 448px;
    height: 560px;
    background: var(--label-bg);
    color: var(--accent);
  }
  .label--white { --accent: var(--gold); --accent-deep: var(--gold-deep); }
  .label--red { --accent: var(--teal); --accent-deep: var(--teal-deep); background: var(--label-bg-red); }

  .lodge { position: absolute; top: 34px; left: 0; right: 0; text-align: center; }
  .lodge__name { font-weight: 700; font-size: 15px; letter-spacing: 0.5px; }
  .lodge__type { font-weight: 400; font-size: 14px; letter-spacing: 0.5px; margin-top: -2px; }

  .rules { position: absolute; left: 0; top: 0; width: 448px; height: 560px; }
  .rules line { stroke: var(--accent); stroke-width: 1.2; }

  .bird {
    position: absolute;
    left: 150px; top: 145px; width: 150px; height: 230px;
    border-radius: 70px 70px 20px 40px;
    background: linear-gradient(180deg, var(--accent-deep) 0%, var(--accent-deep) 55%, var(--accent) 62%, var(--accent) 70%, var(--accent-deep) 78%, rgba(0,0,0,0) 100%);
    opacity: 0.75;
  }

  .vintage {
    position: absolute; left: 62px; top: 182px; width: 66px;
    font-family: "Fascinate Inline", serif;
    font-size: 40px; line-height: 40px; text-align: center;
  }
  .volume { display: block; font-family: "Cinzel", serif; font-size: 13px; line-height: 18px; margin-top: 4px; }

  .place {
    position: absolute; left: 306px; top: 234px;
    font-size: 13px; line-height: 19px;
  }
  .place span { display: block; border-bottom: 1px solid var(--accent); padding: 0 2px; }

  .brand {
    position: absolute; left: 0; right: 0; top: 456px; text-align: center;
    font-family: "Fascinate Inline", serif; font-weight: 400; font-size: 31px; line-height: 44px;
  }
  .varietal {
    position: absolute; left: 0; right: 0; top: 512px; text-align: center;
    font-size: 13px;
  }
</style>
</head>
<body>

<section class="label label--white">
  <svg class="rules" viewBox="0 0 448 560" aria-hidden="true">
    <line x1="28" y1="165" x2="28" y2="440"/><line x1="44" y1="175" x2="44" y2="425"/>
    <line x1="138" y1="175" x2="138" y2="435"/>
    <line x1="310" y1="290" x2="310" y2="420"/><line x1="404" y1="160" x2="404" y2="440"/>
    <line x1="418" y1="175" x2="418" y2="430"/><line x1="432" y1="160" x2="432" y2="445"/>
  </svg>
  <header class="lodge">
    <p class="lodge__name">QUAIL JUBILEE</p>
    <p class="lodge__type">HUNTING LODGE</p>
  </header>
  <div class="bird" role="img" aria-label="Line illustration of a rooster pheasant head and neck with a solid collar band"></div>
  <p class="vintage">20<br>04<span class="volume">750 ML</span></p>
  <p class="place"><span>WILLOW BEND</span><span>NEBRASKA</span></p>
  <h1 class="brand">FEATHERSTONES</h1>
  <p class="varietal">SAUVIGNON BLANC</p>
</section>

<section class="label label--red">
  <svg class="rules" viewBox="0 0 448 560" aria-hidden="true">
    <line x1="28" y1="165" x2="28" y2="440"/><line x1="44" y1="175" x2="44" y2="425"/>
    <line x1="138" y1="175" x2="138" y2="435"/>
    <line x1="310" y1="290" x2="310" y2="420"/><line x1="404" y1="160" x2="404" y2="440"/>
    <line x1="418" y1="175" x2="418" y2="430"/><line x1="432" y1="160" x2="432" y2="445"/>
  </svg>
  <header class="lodge">
    <p class="lodge__name">QUAIL JUBILEE</p>
    <p class="lodge__type">HUNTING LODGE</p>
  </header>
  <div class="bird" role="img" aria-label="Line illustration of a rooster pheasant head and neck with a solid collar band"></div>
  <p class="vintage">20<br>16<span class="volume">750 ML</span></p>
  <p class="place"><span>WILLOW BEND</span><span>NEBRASKA</span></p>
  <h1 class="brand">FEATHERSTONES</h1>
  <p class="varietal">PINOT NOIR</p>
</section>

</body>
</html>
```